ZEK Stationaty Design
ZEK Protection
Project: ZEK Stationaty Design
ZEK Stationaty Design - Security
Creative Brief
Use specific fonts
Agency FB
Professional
Marco VEDI
Directeur
9 Chemin des Tilleuls 1212 Grand-Lancy Genève Suisse
info@zek-protection.example
www.zek-protection.example
Tom482 Tom482
Dear Fraktalgrafik, Vorlo, Thank you for your top designs. We have selected the preferred one with 4 & 5 stars. Could you please submit designs with the top selected business card, and add a A4 page and a email signature designs as well please, any additional stationery design will be great. Thank you in advance, Best regards, Tom

```html
<!DOCTYPE html>
<html lang="fr">
<head>
<meta charset="utf-8">
<title>ZEK Protection – Cartes de visite</title>
<link rel="stylesheet" href="https://fonts.googleapis.com/css2?family=Oswald:wght@300;400;500&display=swap">
<style>
  :root{
    --stage:#e9e6e2;
    --card-black:#111111;
    --card-black-edge:#1c1c1c;
    --card-white:#ffffff;
    --accent:#d3202a;
    --ink:#3a3a3a;
    --ink-soft:#6b6b6b;
    --seal-dark:#2a2a2a;
    --seal-rim:#b9b9b9;
  }
  *{box-sizing:border-box;margin:0;padding:0}
  html,body{width:1200px;height:904px;overflow:hidden}
  body{
    background:var(--stage);
    font-family:"Oswald",sans-serif;
    position:relative;
  }
  .card{
    position:absolute;
    width:600px;height:343px;
    border-radius:22px;
    box-shadow:0 18px 40px rgba(0,0,0,.25);
    overflow:hidden;
  }
  .card--front{
    left:300px;top:70px;
    background:radial-gradient(ellipse at 50% 40%,var(--card-black-edge),var(--card-black) 70%);
  }
  .card--back{
    left:300px;top:491px;
    background:var(--card-white);
  }
  .brand{
    position:absolute;
    display:flex;flex-direction:column;align-items:center;gap:10px;
  }
  .brand__seal{
    border-radius:50%;
    background:var(--seal-dark);
    border:4px solid var(--seal-rim);
  }
  .brand__name{
    font-weight:400;
    letter-spacing:2px;
    text-transform:uppercase;
    white-space:nowrap;
  }
  .card--front .brand{left:50%;top:50%;transform:translate(-50%,-50%)}
  .card--front .brand__seal{width:110px;height:110px}
  .card--front .brand__name{color:#d9d9d9;font-size:15px}

  .card--back .brand{left:60px;top:50%;transform:translateY(-50%)}
  .card--back .brand__seal{width:190px;height:190px}
  .card--back .brand__name{color:var(--seal-dark);font-size:18px}

  .contact{
    position:absolute;left:338px;top:62px;
    color:var(--ink);
  }
  .contact__name{
    color:var(--accent);font-weight:500;font-size:22px;letter-spacing:.5px;line-height:1.1;
  }
  .contact__role{
    font-weight:300;font-size:13px;color:var(--ink-soft);margin-bottom:18px;
  }
  .contact__address{
    font-weight:300;font-size:14px;line-height:1.35;margin-bottom:14px;
  }
  .contact__lines{list-style:none}
  .contact__lines li{
    display:flex;align-items:center;gap:10px;
    font-weight:300;font-size:14px;line-height:1.5;
  }
  .contact__lines svg{width:13px;height:13px;flex:none;fill:var(--accent)}
</style>
</head>
<body>

<section class="card card--front" aria-label="Recto">
  <div class="brand">
    <span class="brand__seal"></span>
    <span class="brand__name">ZEK Protection</span>
  </div>
</section>

<section class="card card--back" aria-label="Verso">
  <div class="brand">
    <span class="brand__seal"></span>
    <span class="brand__name">ZEK Protection</span>
  </div>

  <div class="contact">
    <p class="contact__name">Marco VEDI</p>
    <p class="contact__role">Directeur</p>
    <p class="contact__address">9 Chemin des Tilleuls<br>1299 Montval<br>Vaudrey Suisse</p>
    <ul class="contact__lines">
      <li>
        <svg viewBox="0 0 16 16" aria-hidden="true"><path d="M2 5c0-2 2-3 4-3l1 3-2 1c1 2 3 4 5 5l1-2 3 1c0 2-1 4-3 4C6 14 2 10 2 5z"/></svg>
        +41 22 555 01 10
      </li>
      <li>
        <svg viewBox="0 0 16 16" aria-hidden="true"><rect x="4" y="1" width="8" height="14" rx="1.5"/><rect x="5.5" y="3" width="5" height="8" fill="#fff"/></svg>
        +41 79 555 01 20
      </li>
      <li>
        <svg viewBox="0 0 16 16" aria-hidden="true"><rect x="4" y="1" width="8" height="5"/><rect x="1" y="6" width="14" height="6" rx="1"/><rect x="4" y="10" width="8" height="5" fill="#fff" stroke="#d3202a"/></svg>
        +41 22 555 01 30
      </li>
      <li>
        <svg viewBox="0 0 16 16" aria-hidden="true"><rect x="1" y="3" width="14" height="10" rx="1"/><path d="M2 4l6 5 6-5" fill="none" stroke="#fff" stroke-width="1.5"/></svg>
        info@zek-protection.example
      </li>
      <li>
        <svg viewBox="0 0 16 16" aria-hidden="true"><circle cx="8" cy="8" r="7"/><path d="M1 8h14M8 1c-3 4-3 10 0 14M8 1c3 4 3 10 0 14" fill="none" stroke="#fff" stroke-width="1"/></svg>
        www.zek-protection.example
      </li>
    </ul>
  </div>
</section>

</body>
</html>
```